Info flyer to showcase security camera install and remote video monitoring.

I am looking for an attractive looking flyer that is simple and has some text content and some photos to show prospective clients what services I can provide them.

The two main services that I want to showcase are:
1. Security Camera & NVR Installations and maintenance
2. Remote Video Monitoring for business. This can be a temporary service or ongoing/long term.

Target Market(s)

Construction, Retail, Industrial, Commercial

Industry/Entity Type

Security

Font styles to use
Serif

Colors

Designer to choose colors to be used in the design.

```html
<!DOCTYPE html>
<html lang="en">
<head>
<meta charset="utf-8">
<title>Sentriva Security Systems – Flyer</title>
<link href="https://fonts.googleapis.com/css2?family=Montserrat:wght@500;600;700;800&display=swap" rel="stylesheet">
<style>
  :root {
    --gold: #c9a02a;
    --charcoal: #3a3b3d;
    --ink: #2b2c2e;
    --paper: #ffffff;
    --rule: #4a4a4a;
  }
  * { margin: 0; padding: 0; box-sizing: border-box; }
  html, body { width: 801px; height: 1200px; overflow: hidden; background: var(--paper); }
  .flyer {
    position: relative;
    width: 801px;
    height: 1200px;
    background: var(--paper);
    font-family: "Montserrat", sans-serif;
    color: var(--ink);
  }
  .brand {
    position: absolute;
    left: 38px;
    top: 82px;
  }
  .brand-row { display: flex; align-items: center; gap: 10px; }
  .brand-mark {
    width: 54px; height: 54px;
    border-radius: 50%;
    background: var(--gold);
  }
  .brand-name {
    font-weight: 700;
    font-size: 58px;
    line-height: 1;
    letter-spacing: 1px;
    color: var(--ink);
  }
  .brand-tagline {
    margin-top: 8px;
    font-weight: 600;
    font-size: 25px;
    letter-spacing: 0.5px;
    color: var(--ink);
  }
  .gold-frame {
    position: absolute;
    left: 558px; top: 248px;
    width: 222px; height: 769px;
    background: var(--gold);
  }
  .hero-photo {
    position: absolute;
    left: 0; top: 281px;
    width: 744px; height: 709px;
    background:
      radial-gradient(ellipse 220px 260px at 68% 38%, #e9e6df 0%, #d8d4cc 45%, rgba(216,212,204,0) 75%),
      linear-gradient(180deg, #c9ced3 0%, #aeb6bd 25%, #7d8a95 50%, #4f6a86 72%, #6d7e93 88%, #8b94a1 100%);
  }
  .headline-panel {
    position: absolute;
    left: 0; top: 451px;
    width: 476px; height: 397px;
  }
  .headline-panel svg { position: absolute; inset: 0; }
  .headline-text {
    position: absolute;
    left: 32px; top: 90px;
  }
  .headline {
    font-weight: 800;
    font-size: 30px;
    line-height: 38px;
    letter-spacing: 1.2px;
    color: var(--paper);
    text-transform: uppercase;
  }
  .headline .accent { color: var(--gold); }
  .subhead {
    margin-top: 24px;
    font-weight: 800;
    font-size: 19px;
    line-height: 25px;
    letter-spacing: 0.8px;
    color: var(--gold);
    text-transform: uppercase;
  }
  .subhead .tail { color: var(--gold); }
  .note {
    margin-top: 10px;
    font-weight: 500;
    font-size: 12px;
    color: var(--paper);
  }
  .contact-bar {
    position: absolute;
    left: 0; top: 1040px;
    width: 801px; height: 110px;
  }
  .contact-item {
    position: absolute;
    top: 0;
    width: 220px;
    margin-left: -110px;
    text-align: center;
    font-weight: 600;
    font-size: 11.5px;
    line-height: 15px;
    color: var(--ink);
  }
  .contact-item svg { display: block; margin: 0 auto 12px; }
  .divider {
    position: absolute;
    top: 10px;
    width: 8px; height: 88px;
    border-left: 1.5px solid var(--rule);
    border-right: 1.5px solid var(--rule);
  }
</style>
</head>
<body>
<main class="flyer">
  <header class="brand">
    <div class="brand-row">
      <span class="brand-mark"></span>
      <span class="brand-name">SENTRIVA</span>
    </div>
    <div class="brand-tagline">SECURITY SYSTEMS</div>
  </header>

  <div class="gold-frame"></div>
  <div class="hero-photo" role="img" aria-label="Photo of a white dome security camera mounted from the ceiling inside a busy, softly blurred shopping mall"></div>

  <section class="headline-panel">
    <svg width="476" height="397" viewBox="0 0 476 397" aria-hidden="true">
      <polygon points="0,0 336,0 476,397 0,397" fill="var(--charcoal)"/>
    </svg>
    <div class="headline-text">
      <h1 class="headline">Security<br><span class="accent">Camera &amp; NVR</span><br>Installations<br>and Maintenance</h1>
      <p class="subhead">Remote Video<br>Monitoring for business.</p>
      <p class="note">This can be a temporary service or ongoing/long term.</p>
    </div>
  </section>

  <footer class="contact-bar">
    <div class="contact-item" style="left:138px">
      <svg width="24" height="30" viewBox="0 0 24 30" aria-hidden="true">
        <path d="M12 1C6 1 2 5.5 2 11c0 7 10 18 10 18s10-11 10-18C22 5.5 18 1 12 1z" fill="none" stroke="var(--ink)" stroke-width="3.2"/>
        <circle cx="12" cy="11" r="3.5" fill="var(--ink)"/>
      </svg>
      Lorem Ipsum, Lorem Ipsum<br>Lorem Ipsum Lorem
    </div>
    <span class="divider" style="left:272px"></span>
    <div class="contact-item" style="left:400px">
      <svg width="28" height="30" viewBox="0 0 28 30" aria-hidden="true">
        <path d="M6 2l5 6-3 4c2 4 5 7 9 9l4-3 6 5-3 5C13 28 2 16 1 6z" fill="var(--ink)"/>
      </svg>
      000 000 0000<br>000 000 0000
    </div>
    <span class="divider" style="left:519px"></span>
    <div class="contact-item" style="left:641px">
      <svg width="32" height="22" viewBox="0 0 32 22" style="margin-top:4px" aria-hidden="true">
        <rect x="1" y="1" width="30" height="20" fill="none" stroke="var(--ink)" stroke-width="2"/>
        <path d="M1 1l15 12L31 1M1 21l11-10M31 21L20 11" fill="none" stroke="var(--ink)" stroke-width="2"/>
      </svg>
      <br>info@sentriva.com
    </div>
  </footer>
</main>
</body>
</html>
```